Letterhead for 3 attorney Workers' Comp law firm

We are a 3 attorney law office. We specialize in Workers' Compensation. Our office represents workers who are injured on the job, and the estates of workers who are killed one the job.
When we started our office, we created our own letterhead & have been using it for years. We've just recently hired the 3rd attorney, and were going to just add his name to the letterhead, but have decided we wanted to get a professionally designed letterhead and business cards at this point.
We want something that looks clean and professional. It must look good in black and white because we often make multiple copies of our documents. We're hoping for a design that resonates confidence, reliability and experience.
The design must include the firm name: Dorrance & Pike, PLLC. We would like the PLLC to be small compared to the Dorrance & Pike graphic. We also want to incorporate the attorney names: Ulric Dorrance, Janet Pike, and Lyle Hagberg. Our current letterhead has our contact info in the footer at the bottom of the page. We like that design, but are open to the idea of having it at the top. We'll leave that at the discretion of the designer. Our contact info is as follows: 472 S. Larchmont Avenue, Suite 315 Bellingham, WA 98117 Phone: 360-514-2967, Fax: 360-521-6079, and our website: www.dorrancepike-law.example
Target Market(s)
Clients, courts, other legal offices, doctors offices. These are the people who see our letterhead most frequently. It's not so much for marketing purposes, mainly so that we have a professional image when sending out documents.
Industry/Entity Type
Law Firm
Contact Information for Business Card
On the back of the business card: it can be designed, or be a template for filling in appointment reminder information (i.e. date, time, etc)
Colors
Designer to choose colors to be used in the design.
Requirements
Must have
- Must have our firm name at the top.
- Must include the attorney names.
- Must have all of our contact information (can be at top or bottom - whatever looks best with the design)
Nice to have
- A strong, confident design
Should not have
- We don't want the design to be playful, cartoony or busy.

```html
<!DOCTYPE html>
<html lang="en">
<head>
<meta charset="utf-8">
<title>Dorrance &amp; Pike, PLLC — Letterhead</title>
<link href="https://fonts.googleapis.com/css2?family=Lato:ital,wght@0,400;0,700;1,400;1,700&display=swap" rel="stylesheet">
<style>
  :root {
    --navy: #0f3766;
    --crimson: #9b1b35;
    --paper: #ffffff;
    --ink: #3d3d3d;
    --header-ink: #ffffff;
    --backdrop: #e6e6e6;
  }
  * { margin: 0; padding: 0; box-sizing: border-box; }
  html, body {
    width: 1200px; height: 954px; overflow: hidden;
    background: var(--backdrop);
    font-family: "Lato", Arial, sans-serif;
  }
  .letterhead {
    position: absolute; left: 282px; top: 27px;
    width: 636px; height: 900px;
    background: var(--paper);
    box-shadow: 0 2px 10px rgba(0,0,0,.15);
  }
  .masthead {
    position: absolute; left: 0; top: 0; width: 100%; height: 86px;
    background: var(--navy); color: var(--header-ink);
  }
  .masthead-accent {
    position: absolute; left: 0; top: 82px; width: 240px; height: 4px;
    background: var(--crimson);
  }
  .firm-name {
    position: absolute; left: 40px; top: 22px;
    display: flex; align-items: center; gap: 10px;
    font-weight: 400; font-size: 20px; line-height: 20px; letter-spacing: .5px;
    color: var(--header-ink);
  }
  .firm-mark { width: 26px; height: 26px; border: 1.5px solid var(--header-ink); }
  .firm-name .entity { font-size: 9px; letter-spacing: 1px; }
  .firm-name .lines { display: flex; flex-direction: column; line-height: 21px; }
  .attorneys, .address, .contact {
    position: absolute; top: 26px;
    font-size: 8px; line-height: 12.8px; list-style: none;
  }
  .attorneys { left: 274px; }
  .attorneys li::before { content: "•"; margin-right: 6px; }
  .address { left: 384px; }
  .contact { left: 504px; }
  .letter-body {
    position: absolute; left: 100px; top: 184px; width: 437px;
    color: var(--ink); font-size: 10.6px; line-height: 19.3px;
  }
  .date, .recipient { font-style: italic; font-weight: 700; color: #333; }
  .recipient { margin-top: 9px; line-height: 14.2px; }
  .salutation { margin-top: 22px; }
  .letter-body p.text { margin-top: 17px; text-align: justify; }
  .closing { margin-top: 17px; }
  .signature { margin-top: 14px; line-height: 14.2px; }
</style>
</head>
<body>
  <article class="letterhead">
    <header class="masthead">
      <div class="firm-name">
        <span class="firm-mark"></span>
        <span class="lines"><span>DORRANCE</span><span>&amp; PIKE, <span class="entity">PLLC</span></span></span>
      </div>
      <ul class="attorneys">
        <li>Ulric Dorrance</li>
        <li>Janet Pike</li>
        <li>Lyle Hagberg</li>
      </ul>
      <address class="address" style="font-style:normal">
        472 S. Larchmont Avenue,<br>Suite 315 Bellingham,<br>WA 98117
      </address>
      <div class="contact">
        Phone: 360 514 2967<br>Fax: 360 521 6079<br>www.dorrancepike-law.example
      </div>
    </header>
    <div class="masthead-accent"></div>

    <section class="letter-body">
      <p class="date">March 1, 2001</p>
      <p class="recipient">Mr. Martin Aldous<br>Sample Holdings<br>Suite 12<br>88 Elm Avenue<br>Fernvale, CA 90000</p>
      <p class="salutation">Dear Mr. Aldous,</p>
      <p class="text">This company's letterhead is visually complete only when it displays a typewritten letter. The format of the typewritten message and the quality of execution have a great effect on the attractiveness and impact of the finished letterhead.</p>
      <p class="text">This is the recommended letter format to complement this letterhead design. The letter is typed sinle-spaced in a left-block format with double spacing between paragraps. The typeface we have used in Times New Roman and is set at 12 points. The right margin should not be justified and should not exceed the width of this facsimile letter, and the letter should be centered vertically on the page. In any typed correspondence, great care should be taken to insure that your company's logo is never obstructed in any way. A specific column has been set aside for the symbol which provides it with a presence that ensures that your company's image is consistent, clear and<br>direct.</p>
      <p class="text">Your company's letterhead reflects your standard of quality. Thank you for taking care to produce an attractive and professional letter.</p>
      <p class="closing">Sincerely,</p>
      <p class="signature">Walter Greene,<br>Vice President<br>External Relations</p>
    </section>
  </article>
</body>
</html>
```